Property Management Company looking for a high-end business card, letterhead and envelope design.

We provide high-end / boutique property management for real estate investors or individuals looking for someone to manage their portfolio. we are looking for a cohesive high-end design for our business cards, letterhead and envelopes.

Target Market(s)

Real Estate Investors

Industry/Entity Type

Real Estate

Requirements
Must have
• business card, letterhead and envelope design - logo attached

```html
<!DOCTYPE html>
<html lang="en">
<head>
<meta charset="utf-8">
<title>Stonebay Stationery</title>
<link rel="stylesheet" href="https://fonts.googleapis.com/css2?family=Montserrat:wght@500;600&family=Poppins:wght@400;500&family=Lato:wght@400&display=swap">
<style>
:root{
  --bg:#e6e7e6;
  --paper:#ffffff;
  --navy:#0d4a80;
  --ink:#2b2b2b;
  --muted:#555;
  --rule:#8a8f96;
  --dark-1:#2a2a2a;
  --dark-2:#4a4a4a;
}
*{margin:0;padding:0;box-sizing:border-box}
html,body{width:691px;height:1200px;overflow:hidden}
body{background:var(--bg);position:relative;font-family:"Poppins",sans-serif;color:var(--ink)}
.sheet{position:absolute;background:var(--paper)}
.brand{font-family:"Montserrat",sans-serif;font-weight:600;color:var(--navy);line-height:1}
.brand .name{display:block;letter-spacing:.14em}
.brand .tag{display:block;letter-spacing:.16em}
.contact{position:absolute;border-left:.6px solid var(--rule);font-family:"Poppins",sans-serif;color:var(--ink);line-height:1.45}
.contact .row{display:flex;align-items:center;gap:2px}
.contact svg{flex:none}
.label{position:absolute;font-family:"Lato",sans-serif;color:var(--navy);text-align:center}

/* business cards */
.card-front{left:66px;top:64px;width:118px;height:67px}
.card-front .brand{position:absolute;left:7px;top:28px}
.card-front .brand .name{font-size:7px}
.card-front .brand .tag{font-size:2.6px;margin-top:1px}
.card-front .contact{left:64px;top:11px;padding-left:4px;font-size:2.6px;height:46px}
.card-front .person{font-family:"Montserrat",sans-serif;font-weight:600;font-size:3.8px;color:var(--navy)}
.card-back{left:205px;top:64px;width:119px;height:67px;background:linear-gradient(135deg,var(--dark-2),var(--dark-1))}
.card-back .brand{position:absolute;left:0;right:0;top:27px;text-align:center;color:#fff}
.card-back .brand .name{font-size:7.5px}
.card-back .brand .tag{font-size:2.8px;margin-top:1px}
.card-back .web{position:absolute;left:0;right:0;bottom:5px;text-align:center;font-size:2.5px;color:#ddd}

/* letterheads */
.letterhead{top:165px;height:345px}
.lh-blank{left:70px;width:244px}
.lh-letter{left:363px;width:267px}
.letterhead .brand{position:absolute;left:16px;top:30px}
.letterhead .brand .name{font-size:12.5px}
.letterhead .brand .tag{font-size:5px;margin-top:2px}
.letterhead .contact{top:21px;padding-left:5px;font-size:4.3px}
.lh-blank .contact{left:173px}
.lh-letter .contact{left:188px}
.letter{position:absolute;left:17px;right:17px;top:104px;font-family:"Lato",sans-serif;font-size:3.6px;line-height:1.9;color:var(--ink)}
.letter .salute{color:var(--navy);font-size:4.2px}
.letter p{margin-bottom:5px}
.letter .addr{margin-bottom:9px}
.signature{width:28px;height:10px;background:linear-gradient(90deg,#d9dbe0,#eceef1);border-radius:2px}

/* envelopes */
.env-back{left:59px;top:584px;width:585px;height:261px}
.flap{position:absolute;left:0;top:0;width:585px;height:98px}
.env-back .brand{position:absolute;left:0;right:0;top:37px;text-align:center;color:#fff}
.env-back .brand .name{font-size:18px}
.env-back .brand .tag{font-size:7.6px;margin-top:3px}
.return{position:absolute;left:0;right:0;top:230px;text-align:center;font-size:10.5px;color:var(--ink)}
.return b{color:var(--navy);font-weight:500}
.env-front{left:59px;top:875px;width:585px;height:260px}
.env-front .brand{position:absolute;left:40px;top:40px}
.env-front .brand .name{font-size:21px}
.env-front .brand .tag{font-size:8.4px;margin-top:4px}
</style>
</head>
<body>

<!-- business card, front -->
<section class="sheet card-front">
  <div class="brand"><span class="name">STONEBAY</span><span class="tag">PROPERTY MANAGEMENT</span></div>
  <div class="contact">
    <div class="person">CLARA MENLOW</div>
    <div>President</div>
    <div>4820 Linden Court #210</div>
    <div>Tampa, FL 33611</div>
    <div class="row"><svg width="3" height="3" viewBox="0 0 10 10"><path d="M2 1l2 2-1 1.5a6 6 0 0 0 2.5 2.5L7 6l2 2-1.5 1.5C4 9 1 6 .5 2.5z" fill="#0d4a80"/></svg>+1 (813) 555 0142</div>
    <div class="row"><svg width="3" height="3" viewBox="0 0 10 10"><rect x=".5" y="2" width="9" height="6" fill="none" stroke="#0d4a80"/><path d="M.5 2l4.5 3.5L9.5 2" fill="none" stroke="#0d4a80"/></svg>hello@stonebayhomes.com</div>
    <div class="row"><svg width="3" height="3" viewBox="0 0 10 10"><circle cx="5" cy="5" r="4.5" fill="#0d4a80"/></svg>www.stonebayhomes.com</div>
  </div>
</section>

<!-- business card, back -->
<section class="sheet card-back">
  <div class="brand"><span class="name">STONEBAY</span><span class="tag">PROPERTY MANAGEMENT</span></div>
  <div class="web">www.stonebayhomes.com</div>
</section>

<!-- letterhead, blank -->
<section class="sheet letterhead lh-blank">
  <div class="brand"><span class="name">STONEBAY</span><span class="tag">PROPERTY MANAGEMENT</span></div>
  <div class="contact">
    <div>4820 Linden Court</div>
    <div>#210 Tampa, FL 33611</div>
    <div style="height:3px"></div>
    <div class="row"><svg width="4" height="4" viewBox="0 0 10 10"><path d="M2 1l2 2-1 1.5a6 6 0 0 0 2.5 2.5L7 6l2 2-1.5 1.5C4 9 1 6 .5 2.5z" fill="#0d4a80"/></svg>+1 (813) 555 0142</div>
    <div class="row"><svg width="4" height="4" viewBox="0 0 10 10"><rect x=".5" y="2" width="9" height="6" fill="none" stroke="#0d4a80"/><path d="M.5 2l4.5 3.5L9.5 2" fill="none" stroke="#0d4a80"/></svg>hello@stonebayhomes.com</div>
    <div class="row"><svg width="4" height="4" viewBox="0 0 10 10"><circle cx="5" cy="5" r="4.5" fill="#0d4a80"/></svg>www.stonebayhomes.com</div>
  </div>
</section>

<!-- letterhead, with letter -->
<section class="sheet letterhead lh-letter">
  <div class="brand"><span class="name">STONEBAY</span><span class="tag">PROPERTY MANAGEMENT</span></div>
  <div class="contact">
    <div>4820 Linden Court</div>
    <div>#210 Tampa, FL 33611</div>
    <div style="height:3px"></div>
    <div class="row"><svg width="4" height="4" viewBox="0 0 10 10"><path d="M2 1l2 2-1 1.5a6 6 0 0 0 2.5 2.5L7 6l2 2-1.5 1.5C4 9 1 6 .5 2.5z" fill="#0d4a80"/></svg>+1 (813) 555 0142</div>
    <div class="row"><svg width="4" height="4" viewBox="0 0 10 10"><rect x=".5" y="2" width="9" height="6" fill="none" stroke="#0d4a80"/><path d="M.5 2l4.5 3.5L9.5 2" fill="none" stroke="#0d4a80"/></svg>hello@stonebayhomes.com</div>
    <div class="row"><svg width="4" height="4" viewBox="0 0 10 10"><circle cx="5" cy="5" r="4.5" fill="#0d4a80"/></svg>www.stonebayhomes.com</div>
  </div>
  <div class="letter">
    <div class="salute">Dear, Owen R. Castell</div>
    <div class="addr">President<br>Suite 204<br>2716 Maple Ave<br>Dayton, OH 45402 USA</div>
    <p>Thank you for considering our team to oversee your residential portfolio. We handle tenant screening, lease renewals, routine inspections and monthly reporting so that every property keeps its value and every owner stays informed. Our managers answer calls the same day, track each repair from request to completion, and share clear statements at the close of every month. We would welcome the chance to review your current holdings and outline a plan that fits your goals.</p>
    <p>Our approach is personal and measured. Each client works with one dedicated manager who knows the buildings, the tenants and the local market. We keep vacancy short, costs visible and communication steady throughout the year.</p>
    <p>Please let us know a convenient time to meet. We can visit your properties, answer questions and prepare a written proposal within the week.</p>
    <p>Sincerely</p>
    <div class="signature" role="img" aria-label="Handwritten signature of Clara Menlow"></div>
  </div>
</section>

<div class="label" style="left:70px;width:244px;top:530px;font-size:12px">Letterhead</div>
<div class="label" style="left:363px;width:267px;top:530px;font-size:12px">Word Document Letterhead</div>

<!-- envelope, back -->
<section class="sheet env-back">
  <svg class="flap" viewBox="0 0 585 98" role="img" aria-label="Dark flap with subtle geometric pattern">
    <defs><linearGradient id="flapShade" x1="0" x2="1" y1="0" y2="0"><stop offset="0" stop-color="#2c2c2c"/><stop offset=".5" stop-color="#3e3e3e"/><stop offset="1" stop-color="#2c2c2c"/></linearGradient></defs>
    <path d="M0 0H585L571 82Q568 98 552 98H33Q17 98 14 82Z" fill="url(#flapShade)"/>
  </svg>
  <div class="brand"><span class="name">STONEBAY</span><span class="tag">PROPERTY MANAGEMENT</span></div>
  <div class="return"><b>Stonebay -</b> 4820 Linden Court #210 Tampa, FL 33611</div>
</section>

<!-- envelope, front -->
<section class="sheet env-front">
  <div class="brand"><span class="name">STONEBAY</span><span class="tag">PROPERTY MANAGEMENT</span></div>
</section>

<div class="label" style="left:0;width:691px;top:1150px;font-size:24px">Envelope design</div>

</body>
</html>
```